Skill Up Salary Up

Full Page
7.5 w x 10 h / 8 w x 10.75 h + .25" bleed
Full-Page Career Course Ad
Project Overview
• Goal: Create a visually attractive, modern, and uncluttered full-page magazine advertisement to list available career courses.
• Tone: Creative, professional, and attention-grabbing to prevent the reader from turning the page. The final design must prioritize readability.

Content Requirements
1. Header/Headline: Must be the primary focus. And grab peoples attention
2. Course Listing: A clear, well-organized list of the career courses.
________________________________________
Design & Aesthetic Directives
1. Layout & Readability (Crucial)
• The final ad must not look crowded or busy.
• Prioritize white space to make the text "breathe" and ensure the course list is easy to scan and read.
• Use a modern, clean, and professional typeface (font choice is critical for the aesthetic).
2. Visual Style
• Aim for a creative, modern, and fresh look. Avoid outdated or generic stock imagery/layouts.
3. Imagery/Graphic Element (Artist's Choice)
You have creative freedom regarding the main graphic element.
• Option A (Photography): Use a photo of a white male American with a collared shirt. The imagery should convey success, focus, or professional development.
• Option B (Vector/Illustration): Use a modern vector graphic, illustration, or abstract design. This could be used to symbolize growth, connection, or a career path.
The choice of graphic element is yours, but it must support the overall modern and uncrowded aesthetic.

Requirements
Must have
• Partial listing .. is part of the Vocational Horizon Course

```html
<!DOCTYPE html>
<html lang="en">
<head>
<meta charset="utf-8">
<title>Skill Up, Salary Up – Upcoming KVT Courses</title>
<link href="https://fonts.googleapis.com/css2?family=Rubik:wght@400;500;600;700;800&display=swap" rel="stylesheet">
<style>
:root{
  --navy:#1b4b88;
  --ink:#1d3766;
  --orange:#f7931e;
  --sky:#dde6ef;
  --deep:#1f5a97;
  --chip:#dcdfe4;
  --page:#d5d5d5;
  --white:#ffffff;
}
*{margin:0;padding:0;box-sizing:border-box}
html,body{width:1200px;height:2344px;overflow:hidden;background:var(--page)}
body{font-family:"Rubik",Arial,sans-serif;position:relative}
.ad{position:absolute;left:40px;top:418px;width:947px;height:1275px;transform:scale(1.1827);transform-origin:0 0;background:var(--white);overflow:hidden}
.ad-layer{position:absolute;inset:0;width:947px;height:1275px}
.hero-photo{position:absolute;left:560px;top:0;width:387px;height:345px;background:linear-gradient(135deg,#c9d4de 0%,#e9eef3 45%,#aab8c6 100%)}
.abs{position:absolute}
.headline{left:42px;top:58px;font-weight:800;font-size:38px;line-height:42px;color:var(--navy);letter-spacing:-.3px;white-space:nowrap}
.headline .accent{color:var(--orange)}
.perks{left:46px;top:143px;list-style:none;font-weight:500;font-size:19px;color:var(--navy);line-height:28px}
.perks li{display:flex;align-items:center;gap:8px}
.perks svg{width:16px;height:14px}
.art{position:absolute;border-radius:12px;background:linear-gradient(160deg,#eef2f8,#d6e0ee)}
.course-title{font-weight:700;font-size:27px;line-height:28px;color:var(--navy);letter-spacing:-.2px;white-space:nowrap}
.bullets{list-style:none;font-size:13px;font-weight:500;color:var(--ink);line-height:18px;white-space:nowrap}
.bullets li::before{content:"•";margin-right:6px}
.note{font-size:13px;color:var(--orange);line-height:18px;font-weight:500;white-space:nowrap}
.badge{background:var(--orange);color:var(--white);font-size:10.5px;border-radius:11px;padding:0 10px;height:21px;line-height:21px;white-space:nowrap}
.badge.wide{font-size:15px;height:22px;line-height:22px;border-radius:6px 11px 11px 6px}
.meta{display:flex;height:22px;font-weight:700;font-size:15px;color:var(--navy);line-height:22px;white-space:nowrap}
.meta span{background:var(--chip);padding:0 8px;white-space:nowrap}
.meta span+span{margin-left:4px;clip-path:polygon(10px 0,100% 0,100% 100%,0 100%);padding-left:16px}
.cols{display:flex;gap:0}
</style>
</head>
<body>
<main class="ad">
  <svg class="ad-layer" viewBox="0 0 947 1275" preserveAspectRatio="none" aria-hidden="true">
    <rect width="947" height="370" fill="var(--sky)"/>
  </svg>
  <div class="hero-photo" role="img" aria-label="Two smiling professionals in collared shirts and ties reviewing a tablet by an office window"></div>
  <svg class="ad-layer" viewBox="0 0 947 1275" preserveAspectRatio="none" aria-hidden="true">
    <path d="M0 330 Q470 160 947 345 L947 370 Q470 190 0 345 Z" fill="var(--orange)"/>
    <path d="M0 345 Q470 190 947 370 L947 1275 L0 1275 Z" fill="var(--white)"/>
    <path d="M0 1035 Q470 1200 947 1025 L947 1275 L0 1275 Z" fill="var(--deep)"/>
  </svg>

  <h1 class="abs headline">SKILL UP, <span class="accent">SALARY UP</span><br>UPCOMING KVT COURSES</h1>
  <ul class="abs perks">
    <li><svg viewBox="0 0 16 14"><path d="M2 7l4 4 8-9" fill="none" stroke="#f7931e" stroke-width="3"/></svg>MEN &amp; WOMEN</li>
    <li><svg viewBox="0 0 16 14"><path d="M2 7l4 4 8-9" fill="none" stroke="#f7931e" stroke-width="3"/></svg>IN-PERSON &amp; REMOTE</li>
    <li><svg viewBox="0 0 16 14"><path d="M2 7l4 4 8-9" fill="none" stroke="#f7931e" stroke-width="3"/></svg>PARTIAL SCHOLORASHIPS</li>
  </ul>

  <div class="art" style="left:25px;top:335px;width:160px;height:150px" role="img" aria-label="Illustration of a person ticking items on a large checklist board"></div>
  <h2 class="abs course-title" style="left:201px;top:342px">PARTIAL<br>LISTING</h2>
  <div class="abs cols" style="left:202px;top:405px">
    <ul class="bullets" style="width:111px"><li>Computers</li><li>Marketing</li><li>Sales</li><li>Finance</li><li>Healthcare</li></ul>
    <ul class="bullets"><li>Business Strategy</li><li>Communication</li><li>LedgerPro</li><li>Investments</li><li>Real Estate</li><li>Accounting</li></ul>
  </div>

  <div class="art" style="left:482px;top:335px;width:168px;height:175px" role="img" aria-label="Illustration of a developer coding at a desk surrounded by web windows"></div>
  <h2 class="abs course-title" style="left:659px;top:342px">SOFTWARE,<br>WEB &amp; APPS</h2>
  <div class="abs badge" style="left:660px;top:402px"># 2 Best Tech Job | National Career Review 2025</div>
  <p class="abs note" style="left:663px;top:429px">Job Opportunities</p>
  <ul class="abs bullets" style="left:663px;top:447px"><li>Computer Programmer</li><li>Software Developer/Mobile</li><li>Engineer Developer (Apps</li></ul>
  <p class="abs note" style="left:663px;top:504px">Optional:</p>
  <ul class="abs bullets" style="left:663px;top:520px"><li>&nbsp;Bachelors in Prog. &amp; Tech.</li></ul>
  <div class="abs meta" style="left:662px;top:545px"><span>NOV 2025</span></div>

  <div class="art" style="left:25px;top:585px;width:160px;height:150px" role="img" aria-label="Illustration of a person with charts, invoices and a credit card"></div>
  <h2 class="abs course-title" style="left:201px;top:592px">BOOKKEEPING<br>LEDGERPRO</h2>
  <p class="abs note" style="left:204px;top:652px">Train for a quality job<br>Manage your own books</p>
  <ul class="abs bullets" style="left:204px;top:692px"><li>Finance Management</li><li>Customer &amp; Vendor Mgmt.</li><li>Advanced Tools</li></ul>
  <div class="abs meta" style="left:205px;top:758px"><span style="width:106px">5 WEEKS</span><span style="width:112px">NOV 2025</span></div>

  <div class="art" style="left:482px;top:585px;width:150px;height:180px" role="img" aria-label="Illustration of a technician with a laptop connected to a network of people"></div>
  <h2 class="abs course-title" style="left:657px;top:592px">IT DESKTOP &amp;<br>NETWORKING<br>SUPPORT</h2>
  <div class="abs badge" style="left:658px;top:679px"># 2 Best Tech Job | National Career Review 2025</div>
  <p class="abs note" style="left:661px;top:702px">Masters IT:</p>
  <div class="abs cols" style="left:661px;top:720px">
    <ul class="bullets" style="width:84px"><li>Panora</li><li>Networks</li></ul>
    <ul class="bullets"><li>Servers</li><li>Cloud</li></ul>
  </div>
  <div class="abs meta" style="left:662px;top:766px"><span style="width:108px">7 MONTHS</span><span style="width:108px">DEC 2025</span></div>

  <div class="art" style="left:20px;top:835px;width:168px;height:125px" role="img" aria-label="Illustration of a person working on a laptop beside an app window"></div>
  <h2 class="abs course-title" style="left:201px;top:835px">BRIGHTDESK<br>OFFICE<br>- COMPUTERS</h2>
  <p class="abs note" style="left:204px;top:922px">The New&nbsp;&nbsp; Job Prerequisite</p>
  <div class="abs cols" style="left:204px;top:945px">
    <ul class="bullets" style="width:62px"><li>Gridly</li><li>Scribe</li></ul>
    <ul class="bullets"><li>Mailbox</li><li>SlideKit</li></ul>
  </div>
  <p class="abs note" style="left:204px;top:989px">Computer lab available to practice</p>
  <div class="abs meta" style="left:205px;top:1012px"><span style="width:106px">5 WEEKS</span><span style="width:112px">DEC 2025</span></div>

  <div class="art" style="left:470px;top:835px;width:160px;height:135px" role="img" aria-label="Illustration of two professionals before a globe with a rising growth arrow"></div>
  <h2 class="abs course-title" style="left:657px;top:835px">VOCATIONAL<br>HORIZON</h2>
  <div class="abs badge wide" style="left:658px;top:892px">Business Skills &amp; Knowledge to:</div>
  <ul class="abs bullets" style="left:661px;top:921px"><li>Impress your interviewer</li><li>Maximize Income</li><li>Start / Run Your Business</li></ul>
  <div class="abs meta" style="left:662px;top:985px"><span style="width:116px">4-5 MONTHS</span><span style="width:108px">NOV 2025</span></div>
</main>
</body>
</html>
```